Business Card Design for New Game Studio

We need a business card design. We are a new company developing innovative mobile and platform games.

I would like to see very innovative design thats brings out the company's goal and direction.

My Company's goal and direction is to "Evolve the way of gaming, Bring fun and entertainment to all gamers"

Please do use our company logo which I have attached to be included in the design.

Please put in details for name, title, contacts etc ... be creative !!!

Reason: Company logo redesign. Awaiting it. Thanks

Hi all Please do wait for my updated company logo. Thanks

Reason: Still waiting on new company logo. Thanks all

Hi All Designers .... Sorry for the long wait... Please see the new file for my new company logo uploaded. Waiting to see all your creative design. Cheers

Hi All .... Please do not just mass send a whole bunch of similar designs .... Would like to see quality instead of quantity Cheers

Industry/Entity Type

Entertainment

```html
<!DOCTYPE html>
<html lang="en">
<head>
<meta charset="utf-8">
<title>Quest Harbor – Business Card</title>
<link href="https://fonts.googleapis.com/css2?family=Roboto+Condensed:wght@400;700&display=swap" rel="stylesheet">
<style>
  :root {
    --backdrop: #2b2b2b;
    --card: #ffffff;
    --ink: #1f1f1f;
    --teal: #2f4f5c;
    --green: #8cc63f;
    --muted: #3a3a3a;
  }
  * { box-sizing: border-box; margin: 0; padding: 0; }
  html, body {
    width: 1200px; height: 900px; overflow: hidden;
    background: var(--backdrop);
    font-family: "Roboto Condensed", Arial, sans-serif;
  }
  .stage { position: relative; width: 1200px; height: 900px; }
  .card {
    position: absolute;
    width: 620px; height: 354px;
    background: var(--card);
    overflow: hidden;
    box-shadow: 0 14px 30px rgba(0,0,0,.45);
  }
  /* Front */
  .card--front { left: 60px; top: 70px; }
  .front-mark {
    position: absolute; left: 40px; top: 42px;
    width: 270px; height: 270px; border-radius: 50%;
    background: radial-gradient(circle at 45% 40%, #9bd24a 0%, #8cc63f 35%, #2f5a66 80%, #1f1f1f 100%);
  }
  .front-name {
    position: absolute; left: 340px; top: 150px;
    font-size: 40px; font-weight: 700; color: var(--green);
    letter-spacing: .5px;
  }
  /* Back */
  .card--back { left: 520px; top: 476px; }
  .back-brand {
    position: absolute; left: 34px; top: 112px;
    display: flex; align-items: center; gap: 12px;
  }
  .back-brand__dot {
    width: 56px; height: 56px; border-radius: 50%;
    background: var(--teal);
  }
  .back-brand__name {
    font-size: 30px; font-weight: 700; color: var(--green);
  }
  .contact { position: absolute; left: 318px; top: 44px; color: var(--ink); }
  .contact__name { font-size: 26px; font-weight: 700; color: var(--teal); line-height: 1; }
  .contact__role { font-size: 14px; color: var(--muted); margin-top: 2px; }
  .contact__list { list-style: none; margin-top: 22px; }
  .contact__list li {
    display: flex; align-items: center; gap: 8px;
    font-size: 15px; line-height: 21px; color: var(--ink);
  }
  .contact__list svg { width: 13px; height: 13px; fill: var(--green); flex: none; }
  .office { margin-top: 20px; }
  .office__name { font-size: 17px; font-weight: 700; color: var(--teal); line-height: 1.1; }
  .office__line { font-size: 15px; color: var(--ink); line-height: 1.2; }
  .band {
    position: absolute; bottom: 36px; height: 22px;
  }
  .band--teal { right: 20px; width: 186px; background: var(--teal); }
  .band--green { right: 0; width: 16px; background: var(--green); }
</style>
</head>
<body>
<main class="stage">

  <section class="card card--front" aria-label="Card front">
    <div class="front-mark" role="img" aria-label="Brand emblem area"></div>
    <div class="front-name">Quest Harbor</div>
  </section>

  <section class="card card--back" aria-label="Card back">
    <div class="back-brand">
      <span class="back-brand__dot"></span>
      <span class="back-brand__name">Quest Harbor</span>
    </div>

    <div class="contact">
      <h1 class="contact__name">MIRA DALTON</h1>
      <p class="contact__role">Director</p>
      <ul class="contact__list">
        <li><svg viewBox="0 0 16 16"><path d="M3 1h3l1.5 4-2 1.5a9 9 0 0 0 4 4L11 8.5l4 1.5v3a2 2 0 0 1-2 2A12 12 0 0 1 1 3a2 2 0 0 1 2-2z"/></svg>+65 210 555 014</li>
        <li><svg viewBox="0 0 16 16"><path d="M4 0h8a1 1 0 0 1 1 1v14a1 1 0 0 1-1 1H4a1 1 0 0 1-1-1V1a1 1 0 0 1 1-1zm1 2v10h6V2zm3 11a1 1 0 1 0 0 2 1 1 0 0 0 0-2z"/></svg>+65 210 555 014</li>
        <li><svg viewBox="0 0 16 16"><path d="M0 3h16v10H0zm1 1.2V5l7 4.5L15 5v-.8L8 8.5z"/></svg>hello@questharbor.com</li>
        <li><svg viewBox="0 0 16 16"><path d="M8 0a8 8 0 1 0 0 16A8 8 0 0 0 8 0zm0 1.5c1 0 2 2.4 2.3 5.5H5.7C6 3.9 7 1.5 8 1.5zM5.7 9h4.6C10 12.1 9 14.5 8 14.5S6 12.1 5.7 9z"/></svg>www.questharbor.com</li>
      </ul>
      <div class="office">
        <p class="office__name">QUEST HARBOR</p>
        <p class="office__line">Unit 4, Harbour Lane, 0456</p>
        <p class="office__line">Northbay</p>
      </div>
    </div>

    <div class="band band--teal"></div>
    <div class="band band--green"></div>
  </section>

</main>
</body>
</html>
```